Wealth management firm needs a business card design

Using my logo, create a business card that covers all of the regulatory wordings that I need. It must have - Registered Office 7-9 Pelgrove Wynd, Edinburgh, EH4 2QN. Registered in Scotland under number SC804317. VORELT Wealth Management Ltd is an appointed representative of Kestoby wealth management Ltd, which is authorised and regulated by the Monetary Oversight Council.

Target Market(s)

professional clients

Industry/Entity Type

finance

Contact Information for Business Card

VORELT Wealth Management, Conor Tresk-Whitlaw, Director, 5 Dunmore Row, Edinburgh, EH9 4RT. 07812 459 163, conor.tresk-whitlaw@vorelt-example.com , www.vorelt-example.com

Font styles to use
Serif

Colors
0054AA
0677BA
7BADD7
CADEEF
E8F1F8

Requirements
Must have
• regulatory wording in small text at bottom

```html
<!DOCTYPE html>
<html lang="en">
<head>
<meta charset="utf-8">
<title>VORELT Wealth Management Ltd – Business Card</title>
<link rel="stylesheet" href="https://fonts.googleapis.com/css2?family=Noto+Serif:wght@400;700&display=swap">
<style>
  :root {
    --stage: #2c2c2e;
    --brand-blue: #4176bb;
    --deep-blue: #2447a8;
    --navy: #0c1122;
    --ink: #1a1a1a;
    --paper: #ffffff;
  }
  * { box-sizing: border-box; margin: 0; padding: 0; }
  html, body { width: 1200px; height: 799px; overflow: hidden; }
  body {
    background: var(--stage);
    font-family: "Noto Serif", Georgia, serif;
    position: relative;
  }
  .card {
    position: absolute;
    top: 250px;
    width: 525px;
    height: 300px;
    overflow: hidden;
    box-shadow: 0 14px 30px rgba(0,0,0,.45);
  }
  /* Front */
  .card-front {
    left: 45px;
    background: var(--brand-blue);
    color: var(--paper);
    text-align: center;
  }
  .front-mark {
    width: 78px; height: 78px;
    border-radius: 50%;
    background: var(--paper);
    margin: 56px auto 18px;
  }
  .front-name {
    font-size: 28px;
    font-weight: 400;
    letter-spacing: .3px;
    line-height: 1.15;
    white-space: nowrap;
  }
  .front-tagline {
    font-size: 11px;
    margin-top: 4px;
    letter-spacing: .4px;
  }
  .regulatory {
    position: absolute;
    left: 30px; right: 30px; bottom: 14px;
    font-size: 7px;
    line-height: 1.45;
    opacity: .92;
  }
  /* Back */
  .card-back {
    left: 630px;
    background: var(--paper);
    color: var(--ink);
  }
  .back-wave { position: absolute; left: 0; bottom: 0; width: 525px; height: 300px; }
  .back-brand {
    position: absolute;
    left: 12px; top: 70px;
    width: 226px;
    text-align: center;
  }
  .back-mark {
    width: 40px; height: 40px;
    border-radius: 50%;
    background: var(--brand-blue);
    margin: 0 auto 8px;
  }
  .back-name { font-size: 13px; white-space: nowrap; }
  .back-tagline { font-size: 6.5px; margin-top: 2px; }
  .divider {
    position: absolute;
    left: 250px; top: 58px;
    width: 2px; height: 118px;
    background: var(--deep-blue);
  }
  .contact {
    position: absolute;
    left: 270px; top: 52px;
  }
  .person-name {
    color: var(--brand-blue);
    font-size: 19px;
    font-weight: 700;
    white-space: nowrap;
  }
  .person-role { font-size: 11px; font-weight: 700; margin-bottom: 9px; }
  .contact-list { list-style: none; font-size: 11px; line-height: 1.55; }
  .contact-list li { display: flex; align-items: center; gap: 6px; }
  .contact-list svg { width: 10px; height: 10px; fill: var(--brand-blue); flex: none; }
  .address { font-size: 11px; line-height: 1.45; margin-top: 8px; }
</style>
</head>
<body>
  <section class="card card-front">
    <div class="front-mark"></div>
    <h1 class="front-name">VORELT Wealth Management Ltd</h1>
    <p class="front-tagline">Personal Financial Advice</p>
    <p class="regulatory">Registered Office 7-9 Pelgrove Wynd, Edinburgh, EH4 2QN. Registered in Scotland under number SC804317.<br>VORELT Wealth Management Ltd is an appointed representative of Kestoby wealth management Ltd,<br>which is authorised and regulated by the Monetary Oversight Council.</p>
  </section>

  <section class="card card-back">
    <svg class="back-wave" viewBox="0 0 525 300" preserveAspectRatio="none" aria-hidden="true">
      <path d="M0 222 C90 270 200 288 525 290 L525 300 L0 300 Z" fill="var(--navy)"/>
      <path d="M60 248 C190 282 330 280 525 272 L525 290 C320 292 170 286 60 248 Z" fill="var(--brand-blue)"/>
      <path d="M60 248 C170 286 320 292 525 290" fill="none" stroke="var(--paper)" stroke-width="2"/>
    </svg>

    <div class="back-brand">
      <div class="back-mark"></div>
      <p class="back-name">VORELT Wealth Management Ltd</p>
      <p class="back-tagline">Personal Financial Advice</p>
    </div>

    <div class="divider"></div>

    <div class="contact">
      <p class="person-name">Conor Tresk-Whitlaw</p>
      <p class="person-role">Director</p>
      <ul class="contact-list">
        <li><svg viewBox="0 0 10 10"><path d="M2 0.5 L3.6 2.6 L2.8 3.6 C3.4 5 4.8 6.4 6.3 7.1 L7.3 6.3 L9.5 8 L8.5 9.5 C4.5 9.5 0.5 5.5 0.5 1.5 Z"/></svg>123 456 789</li>
        <li><svg viewBox="0 0 10 10"><path d="M0.5 2 H9.5 V8 H0.5 Z M0.9 2.4 L5 5.4 L9.1 2.4" stroke="#fff" stroke-width=".6"/></svg>info@yourmail-example.com</li>
        <li><svg viewBox="0 0 10 10"><circle cx="5" cy="5" r="4.5"/></svg>www.yoursite-example.com</li>
      </ul>
      <p class="address">5 Dunmore Row,<br>Edinburgh, EH9 4RT</p>
    </div>
  </section>
</body>
</html>
```